Farhan Jewellers Stationary Contest

Pakistan’s largest Jewellery, Diamond and luxury watches store requires professional stationery. We have a long list of are trusted clients since 1959, our third generation has successfully maintained and sustained the legacy and excellence in the sector.

We require stationery template as part of this contest. The stationery can be double sided.

We prefer a design that makes use of some of the premium business stationery printing options, such as foil stamping, embossing/debossing, painted edges, spot UV etc (doesn't have to use all these options, only what you feel works, but we are looking for a design that stands out and is memorable and these nice touches have that effect.)

We want an eye catching, innovative, high end professional looking stationery for an out of box design that blends well with our new logo (attached). We want the design to be an out of box solution, you may use any element to compliment the logo. You may consider incorporating watermark etc, highlighting our products (Gold and Diamond Jewellery in addition to Luxury watches)

Company details are as follows;

Company name: Farhan Jewellers
Contact Person: Tariq Naveed
Designation: Business Development Consultant
Mobile: +92 333 815 6042
Email: tariqnaveed@mailvora.com
Website: www.farhanjewellers-pk.net

Target Market(s)

Matrimonial, Elite & Businesses class, Upmarket

Font styles to use
Other font styles liked:
• Designers choice

Colors

Designer to choose colors to be used in the design.

Requirements
Must have
• Look and feel: Upmarket, innovative, Modern, Professional, graceful, Elegant, designer stuff.
Nice to have
• Unique design

```html
<!DOCTYPE html>
<html lang="en">
<head>
<meta charset="utf-8">
<title>Farhan Jewellers – Business Card</title>
<link href="https://fonts.googleapis.com/css2?family=Open+Sans:wght@400;600;700&display=swap" rel="stylesheet">
<style>
  :root {
    --bg: #cfd3d3;
    --paper: #f3f3f1;
    --gold: #c98f1e;
    --gold-edge: #b87712;
    --ink: #4d4d4d;
    --rule: #8a8a8a;
  }
  * { margin: 0; padding: 0; box-sizing: border-box; }
  html, body {
    width: 1200px; height: 1050px; overflow: hidden;
    background: var(--bg);
    font-family: "Open Sans", Arial, sans-serif;
  }
  .canvas {
    position: relative; width: 1200px; height: 1050px;
    display: flex; flex-direction: column; align-items: center; justify-content: center; gap: 64px;
  }
  .card {
    position: relative; width: 640px; height: 366px;
    background: var(--paper);
    border-bottom: 4px solid var(--gold-edge);
  }
  /* Front */
  .brand {
    position: absolute; top: 58px; left: 0; right: 0;
    display: flex; flex-direction: column; align-items: center; gap: 14px;
  }
  .brand-dot {
    width: 26px; height: 26px; border-radius: 50%; background: var(--gold);
  }
  .brand-name {
    font-weight: 600; font-size: 30px; letter-spacing: 3px;
    color: var(--gold); text-transform: uppercase;
  }
  .details {
    position: absolute; top: 210px; left: 0; right: 0;
    display: flex; justify-content: center; align-items: stretch; gap: 26px;
  }
  .person { text-align: right; padding-top: 6px; }
  .person-name { font-weight: 700; font-size: 19px; color: var(--gold); }
  .person-title { font-size: 13px; color: var(--ink); margin-top: 3px; }
  .divider { width: 1px; background: var(--rule); }
  .contacts { list-style: none; display: flex; flex-direction: column; gap: 6px; }
  .contacts li {
    display: flex; align-items: center; gap: 9px;
    font-size: 13px; color: var(--ink);
  }
  .contacts svg { width: 12px; height: 12px; flex: none; }
  /* Back */
  .back-mark {
    position: absolute; inset: 0;
    display: flex; flex-direction: column; align-items: center; justify-content: center; gap: 16px;
  }
  .back-mark .brand-dot { width: 64px; height: 64px; }
  .back-mark .brand-name { font-size: 22px; }
</style>
</head>
<body>
<main class="canvas">
  <section class="card card-front">
    <div class="brand">
      <span class="brand-dot"></span>
      <span class="brand-name">Farhan Jewellers</span>
    </div>
    <div class="details">
      <div class="person">
        <p class="person-name">Tariq Naveed</p>
        <p class="person-title">Business Development Consultant</p>
      </div>
      <span class="divider"></span>
      <ul class="contacts">
        <li>
          <svg viewBox="0 0 12 12"><path d="M3 1 L5 3.5 L4 5 Q5 7 7 8 L8.5 7 L11 9 L9.5 11 Q5 11 1 3 Z" fill="var(--gold)"/></svg>
          +92 333 815 6042
        </li>
        <li>
          <svg viewBox="0 0 12 12"><rect x="1" y="2.5" width="10" height="7" rx="1" fill="var(--gold)"/><path d="M1.5 3 L6 6.5 L10.5 3" stroke="var(--paper)" fill="none"/></svg>
          tariqnaveed@mailvora.com
        </li>
        <li>
          <svg viewBox="0 0 12 12"><circle cx="6" cy="6" r="5" fill="var(--gold)"/><path d="M1 6 H11 M6 1 Q3 6 6 11 M6 1 Q9 6 6 11" stroke="var(--paper)" stroke-width="0.8" fill="none"/></svg>
          www.farhanjewellers-pk.net
        </li>
      </ul>
    </div>
  </section>

  <section class="card card-back">
    <div class="back-mark">
      <span class="brand-dot"></span>
      <span class="brand-name">Farhan Jewellers</span>
    </div>
  </section>
</main>
</body>
</html>
```